Upgrade Wordpress Website

We have an existing website www.bramblefinch.org.au - we require improved shop, improved donation visibility and interactive forms for sponsorship

```html
<!DOCTYPE html>
<html lang="en">
<head>
<meta charset="utf-8">
<title>Bramblefinch Equine Sanctuary</title>
<link rel="stylesheet" href="https://fonts.googleapis.com/css2?family=Playfair+Display:wght@400;700&family=Poppins:wght@400;500;600&display=swap">
<style>
:root{
  --orange:#e8820f;
  --orange-dark:#d06f05;
  --red:#e0221c;
  --ink:#1d1d1d;
  --text:#444;
  --muted:#666;
  --white:#fff;
  --footer:#262626;
  --light:#f4f4f4;
}
*{box-sizing:border-box;margin:0;padding:0}
html,body{width:1200px;height:4835px;overflow:hidden}
body{position:relative;font-family:"Poppins",sans-serif;color:var(--text);background:var(--white)}
.abs{position:absolute}
.serif{font-family:"Playfair Display",serif;font-weight:400}
.btn{position:absolute;background:var(--orange);color:var(--white);font-size:14px;font-weight:600;display:flex;align-items:center;justify-content:center;gap:6px;text-transform:uppercase;border-radius:2px}
.btn svg{width:13px;height:13px}
.photo{position:absolute}
.rule{position:absolute;height:3px;background:var(--orange)}

/* header */
.topbar{position:absolute;left:0;top:0;width:1200px;height:75px;background:var(--white)}
.brand{position:absolute;left:100px;top:14px;display:flex;align-items:center;gap:10px}
.brand-mark{width:38px;height:38px;background:var(--orange)}
.brand-name{font-family:"Poppins",sans-serif;font-weight:600;color:var(--orange);font-size:15px;line-height:18px;width:120px}
.contact-item{position:absolute;top:18px;display:flex;align-items:center;gap:12px;font-size:15px;font-weight:600;color:var(--ink)}
.ring{width:40px;height:40px;border:2px solid var(--orange);border-radius:50%;display:flex;align-items:center;justify-content:center}
.ring svg{width:18px;height:18px}
.nav{position:absolute;left:0;top:75px;width:1200px;height:43px;background:var(--orange);display:flex;align-items:center}
.nav a{position:absolute;color:var(--white);font-size:14.5px;font-weight:500;text-decoration:none;text-transform:uppercase}

/* hero */
.hero{position:absolute;left:0;top:118px;width:1200px;height:648px;background:linear-gradient(100deg,#5a3a12 0%,#b5781f 35%,#d7a14a 55%,#6b4a22 80%,#2e1c0c 100%)}
.hero h1{position:absolute;left:100px;top:190px;color:var(--white);font-size:54px;line-height:46px;font-family:"Playfair Display",serif;font-weight:400}
.hero p{position:absolute;left:100px;top:310px;width:420px;color:var(--white);font-size:16px;line-height:26px}
.dots{position:absolute;left:563px;top:592px;display:flex;gap:10px}
.dots span{width:12px;height:12px;border:1.5px solid var(--white);border-radius:50%}
.dots span.on{background:var(--white)}

/* sections */
.section-title{position:absolute;left:0;width:1200px;text-align:center;font-family:"Playfair Display",serif;font-weight:400;font-size:50px;color:var(--ink)}
.about p{position:absolute;left:640px;width:460px;font-size:13.5px;line-height:31px;color:var(--text);text-align:justify}
.donate-band{position:absolute;left:0;top:1371px;width:1200px;height:499px;background:linear-gradient(90deg,#f2f0ed 0%,#e6e2dc 50%,#dcd6cf 100%)}
.donate-band p{font-size:15.5px;line-height:24px;color:var(--ink);font-weight:500}

.product{position:absolute;top:2075px;width:238px;text-align:center}
.product .photo{position:relative;width:238px;height:280px}
.stars{margin-top:18px;font-size:12px;color:var(--muted);display:flex;justify-content:center;gap:8px;align-items:center}
.stars b{color:#e6b400;letter-spacing:1px;font-weight:400}
.product h3{margin-top:8px;font-size:14px;line-height:21px;font-weight:500;color:var(--ink);text-transform:uppercase}

.video-band{position:absolute;left:0;top:2526px;width:1200px;height:428px;background:linear-gradient(180deg,#3b362d 0%,#2a2922 60%,#1d2016 100%)}
.video-lower{position:absolute;left:0;top:2954px;width:1200px;height:408px;background:var(--light)}
.video-frame{position:absolute;left:195px;top:2817px;width:812px;height:479px;background:var(--white);padding:7px;box-shadow:0 4px 14px rgba(0,0,0,.15)}

.news{position:absolute;top:3488px;width:324px}
.news .photo{position:relative;width:324px;height:243px}
.news h3{margin-top:15px;font-size:15.5px;line-height:20px;font-weight:600;color:var(--ink)}
.news p{margin-top:8px;font-size:12px;line-height:21px;color:var(--muted)}
.news a{display:block;margin-top:6px;font-size:12.5px;font-weight:600;color:var(--orange);text-decoration:none}

.sponsor{position:absolute;left:0;top:3972px;width:1200px;height:540px;background:linear-gradient(180deg,#e6850f 0%,#df7c09 100%)}
.info{position:absolute;left:116px;display:flex;gap:16px;color:var(--white)}
.info .circle{width:50px;height:50px;border:2px solid var(--white);border-radius:50%;display:flex;align-items:center;justify-content:center;flex:none}
.info .circle svg{width:22px;height:22px}
.info h4{font-size:14.5px;font-weight:600;text-transform:uppercase}
.info p{font-size:14px;line-height:22px}
.field{position:absolute;height:47px;border:1px solid rgba(255,255,255,.85);border-radius:3px;color:var(--white);font-size:13px;display:flex;align-items:flex-start;padding:14px 14px;gap:7px}
.field svg{width:12px;height:12px;margin-top:3px}
.submit{position:absolute;left:794px;width:307px;height:47px;background:var(--red);color:var(--white);font-size:15px;font-weight:600;display:flex;align-items:center;justify-content:center;gap:8px}
.fence-strip{position:absolute;left:0;top:498px;width:1200px;height:42px;background:linear-gradient(180deg,#df7c09 0%,#6a3a10 55%,#2a2a2a 100%)}

.footer{position:absolute;left:0;top:4512px;width:1200px;height:323px;background:var(--footer);color:#ddd}
.footer h5{position:absolute;top:56px;font-family:"Playfair Display",serif;font-weight:400;font-size:17px;color:#eee}
.footer ul{position:absolute;top:90px;list-style:none;font-size:13px;line-height:27px;color:#ddd}
.social{position:absolute;width:30px;height:30px;border-radius:50%;background:#444}
</style>
</head>
<body>

<header class="topbar">
  <div class="brand"><span class="brand-mark"></span><span class="brand-name">Bramblefinch Equine Sanctuary</span></div>
  <div class="contact-item" style="left:427px">
    <span class="ring"><svg viewBox="0 0 24 24" fill="none" stroke="#e8820f" stroke-width="2"><path d="M5 3h4l2 5-3 2a11 11 0 0 0 6 6l2-3 5 2v4a2 2 0 0 1-2 2A17 17 0 0 1 3 5a2 2 0 0 1 2-2z"/></svg></span>0400 555 012
  </div>
  <div class="contact-item" style="left:618px">
    <span class="ring"><svg viewBox="0 0 24 24" fill="none" stroke="#e8820f" stroke-width="2"><rect x="3" y="5" width="18" height="14"/><path d="M3 5l9 8 9-8"/></svg></span>admin@bramblefinch.org.au
  </div>
  <span class="ring abs" style="left:957px;top:18px"></span>
  <span class="ring abs" style="left:1005px;top:18px"><svg viewBox="0 0 24 24" fill="none" stroke="#e8820f" stroke-width="2"><circle cx="12" cy="8" r="4"/><path d="M4 21c1-5 15-5 16 0"/></svg></span>
  <span class="ring abs" style="left:1054px;top:18px"><svg viewBox="0 0 24 24" fill="none" stroke="#e8820f" stroke-width="2"><path d="M5 8h14l-1 13H6z"/><path d="M9 8a3 3 0 0 1 6 0"/></svg></span>
</header>

<nav class="nav">
  <a style="left:100px">Home</a>
  <a style="left:178px">Horses for Adoption</a>
  <a style="left:354px">For Sponsorship</a>
  <a style="left:548px">Shop</a>
  <a style="left:627px">Lease</a>
  <a style="left:710px">Adopted</a>
  <a style="left:820px">Sponsored</a>
  <a style="left:952px">R.I.P</a>
  <a style="left:1020px">Contact</a>
</nav>

<section class="hero" role="img" aria-label="Woman stroking a dark bay horse in a sunlit golden field">
  <h1>Bramblefinch<br>Equine Sanctuary</h1>
  <p>Lorem ipsum dolor sit amet, conseetur adipiscing elit, sed do eiusmod tempor</p>
  <span class="btn" style="left:100px;top:380px;width:147px;height:46px">Donate <svg viewBox="0 0 24 24"><circle cx="12" cy="12" r="11" fill="#fff"/><path d="M10 7l5 5-5 5" stroke="#e8820f" stroke-width="2.5" fill="none"/></svg></span>
  <svg class="abs" style="left:56px;top:300px" width="20" height="36" viewBox="0 0 20 36"><path d="M18 2L3 18l15 16" stroke="#fff" stroke-width="2" fill="none"/></svg>
  <svg class="abs" style="left:1114px;top:300px" width="20" height="36" viewBox="0 0 20 36"><path d="M2 2l15 16L2 34" stroke="#fff" stroke-width="2" fill="none"/></svg>
  <div class="dots"><span></span><span></span><span class="on"></span><span></span></div>
</section>

<section class="about">
  <div class="abs" style="left:124px;top:867px;width:469px;height:412px;background:var(--orange);border-radius:0 0 18px 0"></div>
  <div class="photo" role="img" aria-label="Bay horse with bridle against autumn trees" style="left:113px;top:856px;width:469px;height:412px;background:linear-gradient(135deg,#c86a3a,#7a3b1c 55%,#3a1f10);border-radius:0 0 18px 0"></div>
  <h2 class="abs serif" style="left:640px;top:842px;font-size:50px;color:var(--ink)">About Us</h2>
  <div class="rule" style="left:640px;top:917px;width:90px"></div>
  <p style="top:952px">Bramblefinch Equine Sanctuary (BES) was founded by passionate animal lovers and advocates in 2014, in response to an ever-increasing number of horses passing through the saleyards, and into the hands of knackeries.</p>
  <p style="top:1083px">The name was selected to pay homage to the brilliant protective work done by the Ocean Warden, and to reflect our mission of providing sanctuary and solace to unwanted, injured, and otherwise vulnerable horses</p>
  <span class="btn" style="left:640px;top:1234px;width:168px;height:45px">Learn More <svg viewBox="0 0 24 24"><circle cx="12" cy="12" r="11" fill="#fff"/><path d="M10 7l5 5-5 5" stroke="#e8820f" stroke-width="2.5" fill="none"/></svg></span>
</section>

<section class="donate-band">
  <div class="photo" role="img" aria-label="Young woman embracing a white and chestnut horse" style="left:620px;top:0;width:580px;height:499px;background:linear-gradient(90deg,rgba(230,226,220,0) 0%,#b98e66 30%,#6b4a35 60%,#d9d3cc 100%)"></div>
  <h2 class="abs serif" style="left:100px;top:86px;font-size:50px;color:var(--ink)">DONATE</h2>
  <div class="abs" style="left:100px;top:184px">
    <p>Southvale Bank Account: Bramblefinch Equine Sanctuary<br>BSB: 012 345<br>Account: 100200300</p>
    <p style="margin-top:24px">We are a deductible gift recipient – all donations<br>over $2 are tax deductible.</p>
  </div>
  <span class="btn" style="left:100px;top:353px;width:170px;height:45px">Donate Now <svg viewBox="0 0 24 24"><circle cx="12" cy="12" r="11" fill="#fff"/><path d="M10 7l5 5-5 5" stroke="#e8820f" stroke-width="2.5" fill="none"/></svg></span>
</section>

<section class="shop">
  <h2 class="section-title" style="top:1950px">Our Shop</h2>
  <div class="rule" style="left:555px;top:2030px;width:90px"></div>
  <div class="product" style="left:100px"><div class="photo" role="img" aria-label="Woman in black t-shirt beside a horse" style="background:linear-gradient(160deg,#6d5a48,#b29474 60%,#d8c3a6)"></div><div class="stars"><b>★★★★★</b>(45reviews)</div><h3>Freshly cut lawn- candle<br>BES shaq</h3></div>
  <div class="product" style="left:353px"><div class="photo" role="img" aria-label="Horses eating hay from a red farm cart" style="background:linear-gradient(180deg,#b9c3bb,#7f8c6a 55%,#5b4a36)"></div><div class="stars"><b>★★★★★</b>(45reviews)</div><h3>Freshly cut lawn- candle<br>BES shaq</h3></div>
  <div class="product" style="left:608px"><div class="photo" role="img" aria-label="Calendar cover with horses galloping across grassland" style="background:linear-gradient(180deg,#4f6b3e,#7d8a5c 50%,#a89a78)"></div><div class="stars"><b>★★★★★</b>(45reviews)</div><h3>Freshly cut lawn- candle<br>BES shaq</h3></div>
  <div class="product" style="left:862px"><div class="photo" role="img" aria-label="Horse wearing a blue rug in falling snow" style="background:linear-gradient(160deg,#3e3a40,#2f5e7a 50%,#6c4a32)"></div><div class="stars"><b>★★★★★</b>(45reviews)</div><h3>Freshly cut lawn- candle<br>BES shaq</h3></div>
</section>

<section>
  <div class="video-band" role="img" aria-label="Horses grazing in a field at dusk">
    <h2 class="abs serif" style="left:0;top:58px;width:1200px;text-align:center;font-size:52px;color:var(--white)">Watch Our Video</h2>
    <div class="rule" style="left:555px;top:133px;width:90px"></div>
    <p class="abs" style="left:230px;top:166px;width:740px;text-align:center;color:var(--white);font-size:16.5px;line-height:34px">Lorem ipsum dolor sit amet, consectetur adipiscing elit, sed do eiusmod tempor incididunt ut labore et dolore magna aliqua</p>
  </div>
  <div class="video-lower"></div>
  <div class="video-frame">
    <div role="img" aria-label="Pony wearing a blue winter rug in front of green trees" style="position:relative;width:100%;height:100%;background:linear-gradient(120deg,#4d6a3a,#2f4e86 40%,#263f70 70%,#4d5a3a)">
      <svg class="abs" style="left:351px;top:184px" width="96" height="96" viewBox="0 0 96 96"><circle cx="48" cy="48" r="45" stroke="#fff" stroke-width="3" fill="none"/><path d="M39 30l26 18-26 18z" stroke="#fff" stroke-width="3" fill="none"/></svg>
    </div>
  </div>
</section>

<section>
  <h2 class="section-title" style="top:3378px">Latest News</h2>
  <div class="rule" style="left:555px;top:3460px;width:90px"></div>
  <article class="news" style="left:100px"><div class="photo" role="img" aria-label="Woman in hat standing between horses at a fence" style="background:linear-gradient(180deg,#8fa2a0,#6a5a40 55%,#4a3a2a)"></div><h3>Lorem ipsum dolor sit amet, consectetur adipiscing elit, sed do eiusmod</h3><p>Lorem ipsum dolor sit amet, consectetur adipcing elit, sed do eiusmod tempor incididunt ut labore et dolore magna aliqua.</p><a>READ MORE »</a></article>
  <article class="news" style="left:438px"><div class="photo" role="img" aria-label="Three horses walking across a grassy paddock" style="background:linear-gradient(180deg,#c9d6dc,#a9b27a 55%,#7d8a4c)"></div><h3>Lorem ipsum dolor sit amet, consectetur adipiscing elit, sed do eiusmod</h3><p>Lorem ipsum dolor sit amet, consectetur adipcing elit, sed do eiusmod tempor incididunt ut labore et dolore magna aliqua.</p><a>READ MORE »</a></article>
  <article class="news" style="left:776px"><div class="photo" role="img" aria-label="Rider on a chestnut horse in a dressage arena" style="background:linear-gradient(180deg,#c8d6e0,#4f6a45 45%,#a0623a 75%,#d8d0c0)"></div><h3>Lorem ipsum dolor sit amet, consectetur adipiscing elit, sed do eiusmod</h3><p>Lorem ipsum dolor sit amet, consectetur adipcing elit, sed do eiusmod tempor incididunt ut labore et dolore magna aliqua.</p><a>READ MORE »</a></article>
</section>

<section class="sponsor">
  <div class="info" style="top:123px"><span class="circle"><svg viewBox="0 0 24 24" fill="none" stroke="#fff" stroke-width="2"><path d="M12 22s7-7 7-12a7 7 0 0 0-14 0c0 5 7 12 7 12z"/><circle cx="12" cy="10" r="2.5"/></svg></span><div><h4>Location</h4><p>Bramblefinch Equine Sanctuary<br>Wattle Creek VIC 3999</p></div></div>
  <div class="info" style="top:232px"><span class="circle"><svg viewBox="0 0 24 24" fill="none" stroke="#fff" stroke-width="2"><path d="M5 3h4l2 5-3 2a11 11 0 0 0 6 6l2-3 5 2v4a2 2 0 0 1-2 2A17 17 0 0 1 3 5a2 2 0 0 1 2-2z"/></svg></span><div><h4>Call Us</h4><p>0400 555 012 or 0400 555 034</p></div></div>
  <div class="info" style="top:302px"><span class="circle"><svg viewBox="0 0 24 24" fill="none" stroke="#fff" stroke-width="2"><rect x="3" y="5" width="18" height="14"/><path d="M3 5l9 8 9-8"/></svg></span><div><h4>Email Us</h4><p>admin@bramblefinch.org.au</p></div></div>

  <h2 class="abs serif" style="left:481px;top:84px;font-size:40px;color:var(--white)">Our sponsorship</h2>
  <p class="abs" style="left:481px;top:138px;font-size:15px;font-weight:600;color:var(--white)">Give us a call or use the form below.</p>
  <div class="field" style="left:477px;top:182px;width:304px"><svg viewBox="0 0 24 24" fill="#fff"><circle cx="12" cy="7" r="5"/><path d="M2 23c1-8 19-8 20 0z"/></svg>First Name</div>
  <div class="field" style="left:791px;top:182px;width:308px"><svg viewBox="0 0 24 24" fill="#fff"><circle cx="12" cy="7" r="5"/><path d="M2 23c1-8 19-8 20 0z"/></svg>Last Name</div>
  <div class="field" style="left:477px;top:240px;width:304px"><svg viewBox="0 0 24 24" fill="#fff"><path d="M5 3h4l2 5-3 2a11 11 0 0 0 6 6l2-3 5 2v4a2 2 0 0 1-2 2A17 17 0 0 1 3 5a2 2 0 0 1 2-2z"/></svg>Your phone</div>
  <div class="field" style="left:791px;top:240px;width:308px"><svg viewBox="0 0 24 24" fill="none" stroke="#fff" stroke-width="3"><rect x="3" y="5" width="18" height="14"/></svg>Your Email</div>
  <div class="field" style="left:477px;top:299px;width:622px;height:81px"><svg viewBox="0 0 24 24" fill="#fff"><path d="M3 4h18v12H9l-5 4v-4H3z"/></svg>How Can we help you?</div>
  <div class="submit" style="top:393px">SUBMIT <svg width="15" height="15" viewBox="0 0 24 24" fill="#fff"><path d="M2 11L22 2l-7 20-3-8z"/></svg></div>

  <div class="fence-strip" role="img" aria-label="Dark timber fence line along the edge of the paddock"></div>
</section>

<footer class="footer">
  <div class="abs" style="left:100px;top:60px;display:flex;align-items:center;gap:14px">
    <span style="font-weight:600;font-size:22px;line-height:28px;color:var(--white);width:200px">Bramblefinch Equine Sanctuary</span>
    <span style="width:40px;height:40px;background:var(--white)"></span>
  </div>
  <h5 style="left:410px">Quick Links</h5>
  <ul style="left:410px"><li>Home</li><li>Shop</li><li>Lease</li><li>Adopted</li><li>Sponsored</li><li>Contact</li></ul>
  <h5 style="left:571px">Information</h5>
  <ul style="left:571px"><li>Privacy Policy</li><li>Refund Policy</li><li>Terms &amp; Conditions</li></ul>
  <h5 style="left:778px">Newsletter</h5>
  <p class="abs" style="left:778px;top:90px;width:320px;font-size:13px;line-height:24px">For news, events and updates, subscribe to our newsletter.</p>
  <div class="abs" style="left:778px;top:138px;width:319px;height:43px;background:var(--white);border-radius:3px;display:flex;align-items:center;padding:0 16px;gap:8px;font-size:13px;color:#333">
    <svg width="13" height="13" viewBox="0 0 24 24" fill="#333"><rect x="2" y="4" width="20" height="16"/></svg>Enter your email
    <svg style="margin-left:auto" width="16" height="16" viewBox="0 0 24 24" fill="#e8820f"><path d="M2 11L22 2l-7 20-3-8z"/></svg>
  </div>
  <span class="social" style="left:791px;top:200px"></span>
  <span class="social" style="left:834px;top:200px"></span>
  <span class="social" style="left:877px;top:200px"></span>
  <span class="social" style="left:920px;top:200px"></span>
  <p class="abs" style="left:0;top:290px;width:1200px;text-align:center;font-size:13px;color:#ddd">©2022 bramblefinch. All Rights Reserved.</p>
  <svg class="abs" style="left:1127px;top:255px" width="44" height="44" viewBox="0 0 44 44"><circle cx="22" cy="22" r="22" fill="#e8820f"/><path d="M22 31V13M15 20l7-7 7 7" stroke="#fff" stroke-width="3" fill="none"/></svg>
</footer>

</body>
</html>
```